2020-23 Strategic Plan - Graphic Design Work

We would would like to have our strategic plan designed. It should be two pages.

- I am looking for suggestions on ways to lay this out. I don’t like this boxy layout. It was great for the committee as we went through multiple versions, but I’d prefer the final not follow this boxy format

- I’ve included a few images we own (feel free to use any or none of them). Also attached our logo.

- Have a look at our new website to see our new branding look and feel (launching next week) https://thevorlenta.example-hub.com/

- I've included a copy of our logo.

Target Market(s)

Membership

Other font styles liked:
• Lato

Requirements
Must have
• Excellent layout. Easy to ready. Consistent with branding.

```html
<!DOCTYPE html>
<html lang="en">
<head>
<meta charset="UTF-8">
<title>Institute of Civic Valuers – 2020-2023 Strategic Plan</title>
<link href="https://fonts.googleapis.com/css2?family=Montserrat:wght@800;900&family=Raleway:ital,wght@0,400;0,500;0,600;0,800;1,500&display=swap" rel="stylesheet">
<style>
  :root {
    --backdrop: #e9ece9;
    --paper: #f7f7f7;
    --brand-green: #3b8c35;
    --deep-green: #0e4522;
    --forest: #083a1c;
    --accent-red: #e01b24;
    --panel-green: rgba(76, 150, 62, 0.88);
    --slate: #545454;
    --ink: #222;
    --white: #fff;
  }
  * { margin: 0; padding: 0; box-sizing: border-box; }
  html, body { width: 1070px; height: 1200px; overflow: hidden; }
  body {
    background: var(--backdrop);
    font-family: "Raleway", Arial, sans-serif;
    color: var(--ink);
  }
  .sheet {
    position: absolute;
    left: 115px; top: 0;
    width: 840px; height: 1200px;
    background: var(--paper);
    overflow: hidden;
  }
  .brand {
    position: absolute;
    left: 62px; top: 58px;
    display: flex; align-items: center; gap: 16px;
  }
  .brand-square {
    width: 56px; height: 56px;
    background: var(--brand-green);
    flex-shrink: 0;
  }
  .brand-name {
    font-weight: 800;
    font-size: 28px;
    line-height: 32px;
    color: var(--deep-green);
    letter-spacing: 0.3px;
    width: 230px;
  }
  .website {
    position: absolute;
    right: 66px; top: 88px;
    font-weight: 600;
    font-size: 18px;
    color: var(--deep-green);
    letter-spacing: 0.2px;
  }
  .hero-photo {
    position: absolute;
    left: 0; top: 199px;
    width: 840px; height: 421px;
    background:
      radial-gradient(ellipse at 55% 45%, rgba(225,160,190,0.55), transparent 60%),
      linear-gradient(90deg, #1d2c55 0%, #2f3f78 22%, #6e6aa8 45%, #9d7fb5 58%, #4a3b6e 72%, #26305e 100%);
  }
  .hero-title {
    position: absolute;
    left: 60px; top: 348px;
    color: var(--white);
    line-height: 1;
  }
  .hero-years {
    display: block;
    font-weight: 500;
    font-size: 66px;
    letter-spacing: 1px;
  }
  .hero-heading {
    display: block;
    margin-top: 10px;
    font-weight: 800;
    font-size: 76px;
    letter-spacing: 0.5px;
  }
  .quote-tab {
    position: absolute;
    left: 59px; top: 531px;
    width: 103px; height: 241px;
    background: var(--accent-red);
  }
  .quote-tab svg { position: absolute; left: 27px; top: 104px; }
  .intro {
    position: absolute;
    left: 179px; top: 531px;
    width: 602px; height: 241px;
    background: var(--panel-green);
    padding: 18px 20px 0 18px;
    color: var(--white);
    font-style: italic;
    font-weight: 500;
    font-size: 17.4px;
    line-height: 22.2px;
    text-align: justify;
  }
  .pillar {
    position: absolute;
    top: 808px;
  }
  .pillar h2 {
    font-family: "Montserrat", Arial, sans-serif;
    font-weight: 900;
    font-size: 50px;
    line-height: 1;
    letter-spacing: -0.5px;
  }
  .pillar p {
    margin-top: 12px;
    font-size: 15.6px;
    line-height: 18.8px;
    color: var(--ink);
  }
  .pillar-vision { left: 58px; width: 202px; }
  .pillar-vision h2 { color: var(--brand-green); }
  .pillar-mission { left: 291px; width: 222px; }
  .pillar-mission h2 { color: var(--deep-green); }
  .pillar-values { left: 550px; width: 232px; }
  .pillar-values h2 { color: var(--slate); }
  .footer-band { position: absolute; left: 0; bottom: 0; }
</style>
</head>
<body>
  <main class="sheet">
    <header>
      <div class="brand">
        <span class="brand-square"></span>
        <span class="brand-name">Institute of Civic Valuers</span>
      </div>
      <span class="website">www.thevorlenta.example-hub.com</span>
    </header>

    <div class="hero-photo" role="img" aria-label="Upward view of glass skyscrapers against a streaked purple dusk sky"></div>

    <h1 class="hero-title">
      <span class="hero-years">2020-2023</span>
      <span class="hero-heading">STRAGETIC PLAN</span>
    </h1>

    <div class="quote-tab">
      <svg width="50" height="40" viewBox="0 0 50 40" aria-hidden="true">
        <path d="M2 40V22C2 10 7 3 18 0l2 6c-6 2-8 6-8 12h8v22z" fill="#fff"/>
        <path d="M28 40V22C28 10 33 3 44 0l2 6c-6 2-8 6-8 12h8v22z" fill="#fff"/>
      </svg>
    </div>
    <p class="intro">With over 1,250 members, the Institute of Civic Valuers is Canada’s largest association of property assessment and taxation professionals. Our diverse membership is comprised of individuals from the private and public sectors practicing in the fields of assessment, consultancy, appraisal, taxation and law. Incorporated in May 1957, the ICV is dedicated to advancing the interests, education and professional competence of its members. Our members are highly qualified and widely recognized as the leading professionals in the property assessment industry.</p>

    <section class="pillar pillar-vision">
      <h2>Vision</h2>
      <p>To be the industry leaderin education, ethical standards, and professional accreditation in the field of property assess-ment in Canada.</p>
    </section>
    <section class="pillar pillar-mission">
      <h2>Mission</h2>
      <p>To provide specialized education through a compre-hensive approach to training which embraces all available technologies. To promote professional development and to ensure our members are recognized as experts in the field of property assessment and related functions.</p>
    </section>
    <section class="pillar pillar-values">
      <h2>Values</h2>
      <p>The Institute of Civic Valuers and its members value professionalism, inclusivity, diversity, integrity, ethics, accountability, and expertise. The ICV is committed to serving all members and stakeholders with competence and respect, rejecting all forms of prejudice and discrimination</p>
    </section>

    <svg class="footer-band" width="840" height="66" viewBox="0 0 840 66" aria-hidden="true">
      <path d="M0 0H306L330 20H840V66H0z" fill="var(--forest)"/>
      <path d="M320 11H840V19H330z" fill="var(--brand-green)"/>
      <path d="M336 24H840V30H343z" fill="var(--paper)"/>
    </svg>
  </main>
</body>
</html>
```